Wordpress Design for a Private Label BBQ Brand

For our new brand, we'd need a new Wordpress website. We'd prefer to run the website on Wordpress

We'd like to include the following
- space for description of the brand
- space for product portfolio (not a shop!)
- space for socials
- space for support
- space for contact

```html
<!DOCTYPE html>
<html lang="en">
<head>
<meta charset="utf-8">
<title>Fiammara — Private Label BBQ Brand</title>
<link href="https://fonts.googleapis.com/css2?family=Crimson+Pro:wght@600;700&family=Lato:wght@400;700;900&display=swap" rel="stylesheet">
<style>
:root{
  --orange:#ec5a1c;
  --red:#d3242c;
  --ink:#1b1b1b;
  --text:#444;
  --muted:#666;
  --blue-dark:#1f4a9c;
  --blue:#2f63c0;
  --blue-light:#4c86de;
  --night:#121212;
  --white:#fff;
  --line:#cfcfcf;
}
*{margin:0;padding:0;box-sizing:border-box}
html,body{width:1200px;height:4853px;overflow:hidden}
body{font-family:"Lato",sans-serif;color:var(--ink);background:var(--white);position:relative}
section,header,footer{position:absolute;left:0;width:1200px}
.abs{position:absolute}
.serif{font-family:"Crimson Pro",serif;font-weight:700;letter-spacing:1px}
.btn{position:absolute;display:flex;align-items:center;justify-content:center;border-radius:30px;background:linear-gradient(90deg,var(--orange),var(--red));color:var(--white);font-weight:700;font-size:15px;letter-spacing:.3px}
.eyebrow{color:var(--orange);font-size:30px;font-weight:400;text-transform:uppercase}

/* hero */
.hero{top:0;height:637px;background:radial-gradient(ellipse at 50% 55%,#7a3a1a 0%,#3d1c0e 40%,#120a06 80%)}
.hero-photo{position:absolute;inset:0;background:radial-gradient(ellipse at 20% 90%,rgba(240,120,30,.55),transparent 45%),radial-gradient(ellipse at 85% 85%,rgba(230,90,20,.5),transparent 45%),radial-gradient(ellipse at 50% 40%,rgba(110,60,35,.6),transparent 60%)}
.brand{position:absolute;display:flex;align-items:center;gap:10px;color:var(--white);font-family:"Crimson Pro",serif;font-weight:700;font-size:40px;letter-spacing:1px}
.brand-dot{width:22px;height:22px;border-radius:50%;background:var(--orange)}
.nav a{position:absolute;top:34px;color:var(--white);font-size:15px;font-weight:700;text-decoration:none}
.nav .active::after{content:"";position:absolute;left:0;right:0;top:-34px;height:4px;background:var(--orange)}
.hero-kicker{top:205px;width:100%;text-align:center;color:var(--white);font-size:44px}
.hero-title{top:258px;width:100%;text-align:center;color:var(--white);font-weight:700;font-size:74px;line-height:82px}
.dots{top:589px;left:555px;display:flex;gap:14px;align-items:center}
.dots span{width:8px;height:8px;border-radius:50%;background:rgba(255,255,255,.8)}

/* about */
.about{top:637px;height:452px}
.about p{position:absolute;left:527px;top:122px;width:573px;font-size:15px;line-height:24.5px;color:var(--text)}

/* product description */
.desc{top:1089px;height:1159px;background:radial-gradient(ellipse at 50% 60%,var(--blue-light) 0%,var(--blue) 40%,var(--blue-dark) 100%)}
.center-title{width:100%;text-align:center;color:var(--white)}
.feature{position:absolute;width:260px;margin-left:-130px;text-align:center}
.feature svg{display:block;margin:0 auto}
.feature span{display:block;color:var(--white);font-size:17px;line-height:26px;margin-top:8px}
.kamado{left:471px;top:522px;width:273px;height:405px;border-radius:46% 46% 20% 20%;background:radial-gradient(ellipse at 45% 40%,#3a3a3a,#111 70%)}

/* portfolio */
.portfolio{top:2248px;height:616px;background:linear-gradient(180deg,#f4f6fb,#fff 40%)}
.card{position:absolute;top:213px;width:318px;height:290px;background:var(--white);border-radius:4px;box-shadow:0 6px 22px rgba(0,0,0,.12)}
.card-img{position:absolute;left:40px;top:20px;width:238px;height:205px;border-radius:4px}
.card-label{position:absolute;left:24px;top:250px;font-size:24px}
.card.featured{background:linear-gradient(135deg,var(--orange),var(--red))}
.card.featured .card-label{left:0;width:100%;top:128px;text-align:center;color:var(--white)}

/* support */
.support{top:2864px;height:540px;background:radial-gradient(ellipse at 30% 60%,#3a1e10,#120c09 70%)}
.support-photo{left:100px;top:75px;width:486px;height:415px;background:radial-gradient(ellipse at 70% 40%,#f29a2a,#c4461a 40%,#3a1a0c 85%);border-bottom-right-radius:60px}
.support-frame{left:120px;top:95px;width:486px;height:415px;border-right:2px solid var(--orange);border-bottom:2px solid var(--orange);border-bottom-right-radius:60px}
.support-contact{position:absolute;left:656px;display:flex;align-items:center;gap:14px;color:var(--white);font-weight:700;font-size:16px}

/* social */
.social{top:3404px;height:449px}
.social-box{left:132px;top:162px;width:929px;height:174px;background:var(--white);box-shadow:0 8px 30px rgba(0,0,0,.1)}
.social-item{position:absolute;top:20px;width:180px;margin-left:-90px;text-align:center}
.social-name{display:flex;align-items:center;justify-content:center;gap:6px;height:36px;font-size:17px;font-weight:700;color:var(--ink)}
.social-name i{width:10px;height:10px;background:var(--orange)}
.social-num{font-size:32px;margin-top:10px}
.social-label{font-size:14px;color:var(--muted)}

/* get in touch */
.touch{top:3853px;height:537px;background:linear-gradient(135deg,#e9efe8,#f3f1ea 40%,#e6eef4 75%,#cfe3f0)}
.touch-veil{position:absolute;inset:0;background:linear-gradient(180deg,rgba(255,255,255,.85),rgba(255,255,255,.4) 60%)}
.form{left:317px;top:301px;width:565px;height:311px;background:var(--white);z-index:2}
.field{position:absolute;border:1px solid #999;font-size:14px;padding:12px 9px;color:var(--ink)}

/* footer */
.footer{top:4390px;height:463px;background:var(--night);color:#bbb}
.footer h4{position:absolute;top:156px;color:var(--orange);font-family:"Crimson Pro",serif;font-size:16px;letter-spacing:.8px}
.footer li{list-style:none;position:absolute;font-size:15px;color:#bbb}
.footer li::before{content:"›";color:var(--orange);margin-right:8px}
.contact-row{position:absolute;left:872px;display:flex;gap:14px;font-size:15px;line-height:22px}
.icon-circle{flex:none;width:28px;height:28px;border-radius:50%;background:var(--red);display:flex;align-items:center;justify-content:center}
</style>
</head>
<body>

<header class="hero">
  <div class="hero-photo" role="img" aria-label="Close-up of a grilled steak with rosemary and peppers over open flames"></div>
  <div class="brand" style="left:100px;top:18px"><span class="brand-dot"></span>FIAMMARA</div>
  <nav class="nav">
    <a class="active" style="left:527px">HOME</a>
    <a style="left:631px">ABOUT</a>
    <a style="left:740px">PRODUCT</a>
    <a style="left:870px">SUPPORT</a>
  </nav>
  <div class="btn" style="left:972px;top:23px;width:128px;height:42px">CONTACT ›</div>
  <div class="abs hero-kicker serif">FIAMMARA</div>
  <h1 class="abs hero-title">PRIVATE LABEL<br>BBQ BRAND</h1>
  <div class="btn" style="left:518px;top:443px;width:160px;height:43px">GET STARTED ›</div>
  <svg class="abs" style="left:548px;top:585px" width="14" height="26" viewBox="0 0 14 26"><path d="M12 2 2 13l10 11" fill="none" stroke="#fff" stroke-width="2"/></svg>
  <div class="abs dots"><span></span><span></span><span></span></div>
  <svg class="abs" style="left:632px;top:585px" width="14" height="26" viewBox="0 0 14 26"><path d="M2 2l10 11L2 24" fill="none" stroke="#fff" stroke-width="2"/></svg>
</header>

<section class="about">
  <div class="abs eyebrow" style="left:100px;top:152px">About</div>
  <h2 class="abs serif" style="left:100px;top:182px;font-size:74px;line-height:80px">FIAMMARA</h2>
  <p>Lorem ipsum dolor sit amet, consectetur adipiscing elit. Morbi et ex dui. In hac habitasse platea dictumst. Fusce efficitur purus eu turpis mattis tincidunt et fermentum ligula. Ut eu eros gravida, consequat lacus nec, dignissim urna. Fusce vitae erat sed nisl lobortis imperdiet id vitae massa. Donec ut porttitor purus. Nulla ligula enim, sollicitudin sit amet enim non, pretium lacinia nisi. Pellentesque aliquam posuere gravida.</p>
  <div class="btn" style="left:527px;top:301px;width:164px;height:45px">READ MORE ›</div>
</section>

<section class="desc">
  <div class="abs center-title" style="top:68px;font-size:29px">PRODUCT</div>
  <h2 class="abs center-title serif" style="top:98px;font-size:72px;line-height:80px">DESCRIPTION</h2>

  <div class="feature" style="left:599px;top:192px">
    <svg width="184" height="200" viewBox="0 0 184 200" role="img" aria-label="Bottom damper vent detail"><polygon points="92,3 181,51 181,149 92,197 3,149 3,51" fill="#23314f" stroke="#ec5a1c" stroke-width="2"/><polygon points="92,14 171,57 171,143 92,186 13,143 13,57" fill="#2b2b2b"/></svg>
    <span>Bottom damper to<br>Control airflow</span>
  </div>
  <div class="feature" style="left:356px;top:299px">
    <svg width="184" height="200" viewBox="0 0 184 200" role="img" aria-label="Adjustable top damper detail"><polygon points="92,3 181,51 181,149 92,197 3,149 3,51" fill="#23314f" stroke="#ec5a1c" stroke-width="2"/><polygon points="92,14 171,57 171,143 92,186 13,143 13,57" fill="#2e2e2e"/></svg>
    <span>Adjustable top<br>damper</span>
  </div>
  <div class="feature" style="left:846px;top:299px">
    <svg width="184" height="200" viewBox="0 0 184 200" role="img" aria-label="Stripe surface texture detail"><polygon points="92,3 181,51 181,149 92,197 3,149 3,51" fill="#23314f" stroke="#ec5a1c" stroke-width="2"/><polygon points="92,14 171,57 171,143 92,186 13,143 13,57" fill="#2a2a2a"/></svg>
    <span>Stripe design</span>
  </div>
  <div class="feature" style="left:215px;top:525px">
    <svg width="184" height="200" viewBox="0 0 184 200" role="img" aria-label="Lid thermometer detail"><polygon points="92,3 181,51 181,149 92,197 3,149 3,51" fill="#23314f" stroke="#ec5a1c" stroke-width="2"/><polygon points="92,14 171,57 171,143 92,186 13,143 13,57" fill="#262626"/></svg>
    <span>Temperature Changes<br>Thermometer</span>
  </div>
  <div class="feature" style="left:983px;top:525px">
    <svg width="184" height="200" viewBox="0 0 184 200" role="img" aria-label="Hinge detail"><polygon points="92,3 181,51 181,149 92,197 3,149 3,51" fill="#23314f" stroke="#ec5a1c" stroke-width="2"/><polygon points="92,14 171,57 171,143 92,186 13,143 13,57" fill="#2c2c2c"/></svg>
    <span>Premium Hinge<br>Meterial</span>
  </div>
  <div class="feature" style="left:313px;top:799px">
    <svg width="184" height="200" viewBox="0 0 184 200" role="img" aria-label="Heat insulation handle detail"><polygon points="92,3 181,51 181,149 92,197 3,149 3,51" fill="#23314f" stroke="#ec5a1c" stroke-width="2"/><polygon points="92,14 171,57 171,143 92,186 13,143 13,57" fill="#5a4a2a"/></svg>
    <span>Heat Insulation<br>Handle</span>
  </div>
  <div class="feature" style="left:895px;top:799px">
    <svg width="184" height="200" viewBox="0 0 184 200" role="img" aria-label="Stainless steel mobile cart detail"><polygon points="92,3 181,51 181,149 92,197 3,149 3,51" fill="#23314f" stroke="#ec5a1c" stroke-width="2"/><polygon points="92,14 171,57 171,143 92,186 13,143 13,57" fill="#f2f2f2"/></svg>
    <span style="margin-top:20px">Stainless steel<br>Mobile cart</span>
  </div>

  <div class="abs kamado" role="img" aria-label="Black ceramic kamado grill on a three-leg stand"></div>
</section>

<section class="portfolio">
  <div class="abs eyebrow" style="left:100px;top:72px">Product</div>
  <h2 class="abs serif" style="left:100px;top:102px;font-size:72px;line-height:80px">PORTFOLIO</h2>
  <div class="btn" style="left:938px;top:99px;width:162px;height:46px">VIEW ALL ›</div>

  <div class="card" style="left:98px">
    <div class="card-img" role="img" aria-label="Stainless steel BBQ tool set in a black case" style="background:linear-gradient(135deg,#2a2a2a,#8c8c8c 50%,#1c1c1c)"></div>
    <div class="card-label">BBQ equipment 01</div>
  </div>
  <div class="card featured" style="left:441px">
    <div class="card-label">BBQ equipment 02</div>
  </div>
  <div class="card" style="left:783px">
    <div class="card-img" role="img" aria-label="Black kamado grill on stand" style="background:radial-gradient(ellipse at 50% 35%,#3a3a3a,#121212 40%,#fff 42%)"></div>
    <div class="card-label">BBQ equipment 03</div>
  </div>
</section>

<section class="support">
  <div class="abs support-frame"></div>
  <div class="abs support-photo" role="img" aria-label="Steak with rosemary grilling over high flames"></div>
  <div class="abs serif" style="left:656px;top:148px;color:var(--orange);font-size:29px">NEED SUPPORT</div>
  <h2 class="abs serif" style="left:656px;top:180px;color:var(--white);font-size:54px;line-height:60px">FOR CONTACT US</h2>
  <p class="abs" style="left:656px;top:254px;width:450px;color:#ddd;font-size:15px;line-height:24px">Curabitur ipsum sem, gravida vifelis non, viverra accumsan sem. Integer sollicitudin enim a nisl tincidunt gravida.</p>
  <div class="support-contact" style="top:322px">
    <svg width="18" height="14" viewBox="0 0 18 14"><rect x="1" y="1" width="16" height="12" rx="1" fill="var(--orange)"/><path d="M1 2l8 6 8-6" fill="none" stroke="#120c09" stroke-width="1.5"/></svg>
    info@fiammara.example
  </div>
  <div class="support-contact" style="top:356px">
    <svg width="18" height="18" viewBox="0 0 18 18"><path d="M4 1l3 4-2 2c1 3 3 5 6 6l2-2 4 3-2 3C8 17 1 10 1 4z" fill="var(--orange)"/></svg>
    1800 555 019
  </div>
</section>

<section class="social">
  <h2 class="abs center-title serif" style="top:74px;color:var(--ink);font-size:52px">SOCIAL MEDIA</h2>
  <div class="abs social-box">
    <div class="social-item" style="left:73px"><div class="social-name"><i></i>Pagebook</div><div class="social-num">1,000</div><div class="social-label">Followers</div></div>
    <div class="social-item" style="left:262px"><div class="social-name"><i></i>Chirper</div><div class="social-num">500</div><div class="social-label">Followers</div></div>
    <div class="social-item" style="left:452px"><div class="social-name"><i></i>Snapgram</div><div class="social-num">1,500</div><div class="social-label">Followers</div></div>
    <div class="social-item" style="left:650px"><div class="social-name"><i></i>Streamly</div><div class="social-num">1M</div><div class="social-label">Subscribers</div></div>
    <div class="social-item" style="left:850px"><div class="social-name"><i></i>Linkwork</div><div class="social-num">50</div><div class="social-label">Connection</div></div>
  </div>
</section>

<section class="touch">
  <div class="abs" style="inset:0" role="img" aria-label="City street map of the business location"></div>
  <div class="touch-veil"></div>
  <div class="abs eyebrow" style="left:0;width:100%;text-align:center;top:62px;font-size:28px">Contact Us</div>
  <h2 class="abs center-title serif" style="top:100px;color:var(--ink);font-size:68px;line-height:74px">GET IN TOUCH</h2>
  <div class="abs form">
    <div class="field" style="left:24px;top:24px;width:247px;height:45px">First Name</div>
    <div class="field" style="left:288px;top:24px;width:248px;height:45px">Last Name</div>
    <div class="field" style="left:24px;top:80px;width:247px;height:47px">Phone No.</div>
    <div class="field" style="left:288px;top:80px;width:248px;height:47px">Email</div>
    <div class="field" style="left:24px;top:142px;width:512px;height:88px">Message</div>
    <div class="btn" style="left:214px;top:247px;width:134px;height:43px">SUBMIT ›</div>
  </div>
</section>

<footer class="footer">
  <div class="brand" style="left:100px;top:162px;font-size:44px"><span class="brand-dot"></span>FIAMMARA</div>
  <p class="abs" style="left:100px;top:232px;width:270px;font-size:15px;line-height:24px">Lorem ipsum dolor sit, consectetur adipiscing elit. Nullam eget ante est. Proin placerat mauris vitae luctus eleifend.</p>

  <h4 style="left:448px">NAVIGATION</h4>
  <ul>
    <li style="left:448px;top:200px">Home</li>
    <li style="left:448px;top:238px">About</li>
    <li style="left:448px;top:275px">Product</li>
    <li style="left:448px;top:313px">Support</li>
    <li style="left:448px;top:351px">Contact</li>
  </ul>

  <h4 style="left:624px">PRODUCTS</h4>
  <ul>
    <li style="left:624px;top:200px">BBQ equipment 01</li>
    <li style="left:624px;top:238px">BBQ equipment 02</li>
    <li style="left:624px;top:275px">BBQ equipment 03</li>
    <li style="left:624px;top:313px">BBQ equipment 04</li>
  </ul>

  <h4 style="left:872px">CONTACT US</h4>
  <div class="contact-row" style="top:192px">
    <span class="icon-circle"><svg width="12" height="16" viewBox="0 0 12 16"><path d="M6 15S1 9 1 6a5 5 0 0 1 10 0c0 3-5 9-5 9z" fill="#fff"/><circle cx="6" cy="6" r="2" fill="#d3242c"/></svg></span>
    <span>123 Address line here<br>City Country Lom ipsum</span>
  </div>
  <div class="contact-row" style="top:273px">
    <span class="icon-circle"><svg width="14" height="14" viewBox="0 0 18 18"><path d="M4 1l3 4-2 2c1 3 3 5 6 6l2-2 4 3-2 3C8 17 1 10 1 4z" fill="#fff"/></svg></span>
    <span>1800 555 019</span>
  </div>
  <div class="contact-row" style="top:322px">
    <span class="icon-circle"><svg width="14" height="11" viewBox="0 0 18 14"><rect x="1" y="1" width="16" height="12" fill="#fff"/><path d="M1 2l8 6 8-6" fill="none" stroke="#d3242c" stroke-width="1.5"/></svg></span>
    <span>info@fiammara.example</span>
  </div>

  <div class="abs" style="left:100px;top:405px;width:1000px;height:1px;background:#333"></div>
  <div class="abs" style="left:100px;top:425px;font-size:14px">© 2023 <span style="color:var(--orange)">Fiammara</span>. All right reserved</div>
  <div class="abs" style="left:900px;width:200px;text-align:right;top:425px;font-size:14px">January 10,2023. Layout_4</div>
</footer>

</body>
</html>
```